NGO... Marigold Study Circle, Cambodia

require photo of banyan leaf one side and my info other side. I have an NGO doing village support work plus managing village schools in Cambodia. Require a simple square card with b/w design of leaf.
I am a volunteer organisation and provide small business opportunities for the local families.

Industry/Entity Type

Learning

Contact Information for Business Card

square card, banyan leaf design b/w

Font styles to use
Serif

```html
<!DOCTYPE html>
<html lang="en">
<head>
<meta charset="utf-8">
<title>Marigold Study Circle – Square Business Cards</title>
<link href="https://fonts.googleapis.com/css2?family=Heebo:wght@400;500;600&display=swap" rel="stylesheet">
<style>
  :root {
    --page-bg: #dedbd7;
    --paper-white: #ffffff;
    --paper-black: #231f20;
    --ink-dark: #231f20;
    --ink-mid: #3c3a3b;
    --ink-light: #ffffff;
  }
  * { margin: 0; padding: 0; box-sizing: border-box; }
  html, body {
    width: 1200px;
    height: 750px;
    overflow: hidden;
    background: var(--page-bg);
    font-family: "Heebo", Arial, sans-serif;
  }
  .canvas {
    position: relative;
    width: 1200px;
    height: 750px;
  }
  .card {
    position: absolute;
    width: 320px;
    height: 320px;
    overflow: hidden;
  }
  .card--light { background: var(--paper-white); color: var(--ink-mid); }
  .card--dark  { background: var(--paper-black); color: var(--ink-light); }

  .card--front-light { left: 224px; top: 30px; }
  .card--front-dark  { left: 576px; top: 30px; }
  .card--back-light  { left: 226px; top: 388px; }
  .card--back-dark   { left: 576px; top: 388px; }

  .front {
    position: absolute;
    inset: 0;
    text-align: center;
  }
  .brand {
    position: absolute;
    top: 38px;
    width: 100%;
    line-height: 1;
  }
  .brand__name {
    display: block;
    font-size: 30px;
    font-weight: 500;
    letter-spacing: 0.3px;
  }
  .brand__tagline {
    display: block;
    margin-top: 3px;
    font-size: 16.5px;
    font-weight: 500;
  }
  .card--light .brand { color: var(--ink-dark); }

  .person {
    position: absolute;
    top: 121px;
    width: 100%;
    line-height: 1;
  }
  .person__name {
    display: block;
    font-size: 22px;
    font-weight: 400;
  }
  .person__role {
    display: block;
    margin-top: 10px;
    font-size: 14.5px;
    font-weight: 600;
  }
  .contact {
    position: absolute;
    top: 192px;
    width: 100%;
    list-style: none;
    font-size: 15px;
    letter-spacing: 0.6px;
    line-height: 19px;
  }
  .contact li {
    display: flex;
    justify-content: center;
    align-items: center;
    gap: 4px;
  }
  .contact li.contact__address { margin-top: 3px; }
  .icon { width: 14px; height: 14px; flex: none; fill: currentColor; }

  .leaf-art {
    position: absolute;
    left: 0;
    top: 0;
    width: 220px;
    height: 215px;
    border-radius: 0 90px 140px 30px;
  }
  .card--back-light .leaf-art {
    background: linear-gradient(160deg, #231f20 0%, #3a3637 100%);
  }
  .card--back-dark .leaf-art {
    background: linear-gradient(160deg, #ffffff 0%, #e6e4e3 100%);
  }
</style>
</head>
<body>
<main class="canvas">

  <!-- Front, white stock -->
  <section class="card card--light card--front-light">
    <div class="front">
      <h1 class="brand">
        <span class="brand__name">Marigold</span>
        <span class="brand__tagline">Study Circle</span>
      </h1>
      <p class="person">
        <span class="person__name">Sophea Ranvel</span>
        <span class="person__role">Deractor</span>
      </p>
      <ul class="contact">
        <li><svg class="icon" viewBox="0 0 24 24"><path d="M6.6 10.8a15 15 0 0 0 6.6 6.6l2.2-2.2c.3-.3.7-.4 1-.2 1.1.4 2.3.6 3.6.6.6 0 1 .4 1 1V20c0 .6-.4 1-1 1A17 17 0 0 1 3 4c0-.6.4-1 1-1h3.5c.6 0 1 .4 1 1 0 1.3.2 2.5.6 3.6.1.3 0 .7-.2 1z"/></svg>+ 855-221-904</li>
        <li><svg class="icon" viewBox="0 0 24 24"><path d="M2 9l10-6 10 6v11H2zm2 1.2V18h16v-7.8l-8 5z"/></svg>hi@marigold.org</li>
        <li><svg class="icon" viewBox="0 0 24 24"><path d="M12 2a10 10 0 1 0 0 20 10 10 0 0 0 0-20zm6.9 9h-3a15 15 0 0 0-1.2-5.5A8 8 0 0 1 18.9 11zM12 4.1c.9 1.3 1.7 3.7 1.9 6.9h-3.8c.2-3.2 1-5.6 1.9-6.9zM9.3 5.5A15 15 0 0 0 8.1 11h-3a8 8 0 0 1 4.2-5.5zM5.1 13h3a15 15 0 0 0 1.2 5.5A8 8 0 0 1 5.1 13zm6.9 6.9c-.9-1.3-1.7-3.7-1.9-6.9h3.8c-.2 3.2-1 5.6-1.9 6.9zm2.7-1.4a15 15 0 0 0 1.2-5.5h3a8 8 0 0 1-4.2 5.5z"/></svg>marigold.org</li>
        <li class="contact__address"><svg class="icon" viewBox="0 0 24 24"><path d="M12 2a7 7 0 0 0-7 7c0 5 7 13 7 13s7-8 7-13a7 7 0 0 0-7-7zm0 9.5A2.5 2.5 0 1 1 12 6.5a2.5 2.5 0 0 1 0 5z"/></svg>14 Wat Bo Road, Siem Reap</li>
      </ul>
    </div>
  </section>

  <!-- Front, black stock -->
  <section class="card card--dark card--front-dark">
    <div class="front">
      <h2 class="brand">
        <span class="brand__name">Marigold</span>
        <span class="brand__tagline">Study Circle</span>
      </h2>
      <p class="person">
        <span class="person__name">Sophea Ranvel</span>
        <span class="person__role">Deractor</span>
      </p>
      <ul class="contact">
        <li><svg class="icon" viewBox="0 0 24 24"><path d="M6.6 10.8a15 15 0 0 0 6.6 6.6l2.2-2.2c.3-.3.7-.4 1-.2 1.1.4 2.3.6 3.6.6.6 0 1 .4 1 1V20c0 .6-.4 1-1 1A17 17 0 0 1 3 4c0-.6.4-1 1-1h3.5c.6 0 1 .4 1 1 0 1.3.2 2.5.6 3.6.1.3 0 .7-.2 1z"/></svg>+ 855-221-904</li>
        <li><svg class="icon" viewBox="0 0 24 24"><path d="M2 9l10-6 10 6v11H2zm2 1.2V18h16v-7.8l-8 5z"/></svg>hi@marigold.org</li>
        <li><svg class="icon" viewBox="0 0 24 24"><path d="M12 2a10 10 0 1 0 0 20 10 10 0 0 0 0-20zm6.9 9h-3a15 15 0 0 0-1.2-5.5A8 8 0 0 1 18.9 11zM12 4.1c.9 1.3 1.7 3.7 1.9 6.9h-3.8c.2-3.2 1-5.6 1.9-6.9zM9.3 5.5A15 15 0 0 0 8.1 11h-3a8 8 0 0 1 4.2-5.5zM5.1 13h3a15 15 0 0 0 1.2 5.5A8 8 0 0 1 5.1 13zm6.9 6.9c-.9-1.3-1.7-3.7-1.9-6.9h3.8c-.2 3.2-1 5.6-1.9 6.9zm2.7-1.4a15 15 0 0 0 1.2-5.5h3a8 8 0 0 1-4.2 5.5z"/></svg>marigold.org</li>
        <li class="contact__address"><svg class="icon" viewBox="0 0 24 24"><path d="M12 2a7 7 0 0 0-7 7c0 5 7 13 7 13s7-8 7-13a7 7 0 0 0-7-7zm0 9.5A2.5 2.5 0 1 1 12 6.5a2.5 2.5 0 0 1 0 5z"/></svg>14 Wat Bo Road, Siem Reap</li>
      </ul>
    </div>
  </section>

  <!-- Back, white stock -->
  <section class="card card--light card--back-light">
    <div class="leaf-art" role="img" aria-label="Black banyan leaf illustration with white veins, stem trailing to the lower right"></div>
  </section>

  <!-- Back, black stock -->
  <section class="card card--dark card--back-dark">
    <div class="leaf-art" role="img" aria-label="White banyan leaf illustration with dark veins, stem trailing to the lower right"></div>
  </section>

</main>
</body>
</html>
```